SkyVelour IOS App for iPhone / Luxury private aviation / 1 main screen

Hello there !

SkyVelour Ltd is a VIP aircraft operator. You can see our https://social-example.net/skyvelour page or our https://photo-example.net/sky_velour . Our web page http://skyvelour-demo.net says it all, we don't communicate much except for the music industry activities we have.

We have developed a very simple app, 6 screens total, that will give the user a distance and a flight time between any two airports of the world. Enter a departure point (New York or JFK or KJFK...) and a destination (like Los Angeles, LAX or KLAX) and we will give you the flight time depending on the type of private jet you are selecting in the aircraft database of the app.

You might want to see the attached pdf for the flow...Any design idea is welcome.

We want it to be simple, pure, fast, and of course less will be more. We should see a unity between all these screens, same design spirit of course... On the main screen of the app, we are showing:- the company logo- a departure airport- a destination airport- the selected aircraft with access to a mini photo gallery of the said airplane- a flight time shown in hours and minutes- a distance shown in Miles, Nautical Miles or KM according to the pref page selection- an access to a contact screen- an access to a parameters screen (will develop some of it on a later version).

Thanks !!

Mathis

Target Market(s)

Private aircraft travelers and VIP flights brokers

Industry/Entity Type

Aviation

Font styles to use
Sans Serif

Colors
aaaaaa
5c5c5c
1b1b1b
e9e9e9
ffffff

Requirements
Must have
• Our logo
Nice to have
• Elegant design
Should not have
• Complicated stuff

```html
<!DOCTYPE html>
<html lang="en">
<head>
<meta charset="utf-8">
<title>SkyVelour – Main Screen</title>
<link rel="stylesheet" href="https://fonts.googleapis.com/css2?family=Barlow:wght@200;300;400;500&display=swap">
<style>
  :root {
    --screen-top: #eaeae7;
    --screen-bottom: #bcbcbc;
    --panel: #dcdcdc;
    --ink: #1b1b1b;
    --ink-soft: #5c5c5c;
    --rule: #8f8f8f;
    --icon: #aaaaaa;
    --accent: #2f6fc0;
    --thumb-dark: #4a4a4a;
    --thumb-light: #d8d8d8;
    --white: #ffffff;
  }
  * { box-sizing: border-box; margin: 0; padding: 0; }
  html, body { width: 829px; height: 1200px; overflow: hidden; }
  body { font-family: "Barlow", sans-serif; color: var(--ink); }

  .app-screen {
    position: relative;
    width: 829px;
    height: 1200px;
    background: linear-gradient(180deg, var(--screen-top) 0%, #e2e2df 45%, var(--screen-bottom) 100%);
    overflow: hidden;
  }

  /* status bar */
  .status-time {
    position: absolute; left: 62px; top: 28px;
    font-size: 20px; font-weight: 400; color: var(--icon);
  }
  .status-icons {
    position: absolute; right: 40px; top: 30px;
    display: flex; gap: 12px; align-items: center;
  }

  /* top bar */
  .menu-button { position: absolute; left: 52px; top: 86px; width: 34px; height: 24px; }
  .contact-button { position: absolute; left: 760px; top: 84px; width: 36px; height: 28px; }

  /* brand */
  .brand {
    position: absolute; left: 0; right: 0; top: 330px;
    display: flex; flex-direction: column; align-items: center; gap: 26px;
  }
  .brand-circle {
    width: 70px; height: 70px; border-radius: 50%;
    border: 2px solid var(--ink-soft);
  }
  .brand-name {
    font-size: 54px; font-weight: 300; letter-spacing: 20px;
    text-transform: uppercase; color: var(--ink-soft);
    padding-left: 20px;
  }

  /* route */
  .route { position: absolute; left: 35px; right: 39px; top: 538px; height: 120px; }
  .route-rule { position: absolute; height: 1px; background: var(--rule); }
  .route-rule.top-left { left: 0; width: 318px; top: 0; }
  .route-rule.top-right { right: 0; width: 315px; top: 0; }
  .route-rule.bottom-left { left: 0; width: 318px; top: 118px; }
  .route-rule.bottom-right { right: 0; width: 315px; top: 118px; }
  .airport {
    position: absolute; top: 22px; width: 318px; text-align: center;
  }
  .airport.departure { left: 0; }
  .airport.destination { right: 0; width: 315px; }
  .airport-label { font-size: 22px; font-weight: 400; color: var(--ink-soft); }
  .airport-code { font-size: 58px; font-weight: 200; letter-spacing: 3px; line-height: 1.15; color: var(--ink-soft); }
  .go-button {
    position: absolute; left: 340px; top: 20px; width: 78px; height: 78px;
  }
  .aircraft-code {
    position: absolute; left: 318px; width: 121px; top: 104px;
    text-align: center; font-size: 20px; font-weight: 400; color: var(--ink-soft);
  }

  /* flight details */
  .details {
    position: absolute; left: 35px; top: 697px; width: 755px; height: 278px;
    background: var(--panel);
    display: flex; flex-direction: column; align-items: center;
    padding-top: 40px;
  }
  .detail-row { display: flex; align-items: baseline; gap: 6px; color: var(--ink); }
  .detail-label { font-size: 17px; font-weight: 400; text-transform: uppercase; letter-spacing: 0.5px; color: var(--ink-soft); }
  .detail-value { font-size: 30px; font-weight: 400; color: #333; }
  .detail-row + .detail-row { margin-top: 4px; }
  .detail-row.aircraft { margin-top: 38px; }

  .gallery {
    display: flex; gap: 8px; margin-top: 10px;
  }
  .gallery-photo { width: 106px; height: 72px; }
  .gallery-photo.exterior { background: linear-gradient(180deg, #9a9a9a 0%, var(--thumb-light) 55%, #7a7a7a 100%); }
  .gallery-photo.runway { background: linear-gradient(180deg, #5f5f5f 0%, #b8b8b8 50%, var(--thumb-light) 100%); }
  .gallery-photo.stairs { background: linear-gradient(180deg, var(--thumb-dark) 0%, #9c9c9c 60%, #6a6a6a 100%); }
  .gallery-photo.cabin { background: linear-gradient(180deg, #2c2c2c 0%, #8c8c8c 55%, #3c3c3c 100%); }

  .home-indicator {
    position: absolute; left: 267px; top: 1180px; width: 295px; height: 6px;
    border-radius: 3px; background: #8a8a8a;
  }
</style>
</head>
<body>
<main class="app-screen">
  <div class="status-time">5:30</div>
  <div class="status-icons" aria-hidden="true">
    <svg width="28" height="18" viewBox="0 0 28 18"><rect x="0" y="12" width="4" height="6" fill="#aaaaaa"/><rect x="7" y="8" width="4" height="10" fill="#aaaaaa"/><rect x="14" y="4" width="4" height="14" fill="#aaaaaa"/><rect x="21" y="0" width="4" height="18" fill="#aaaaaa"/></svg>
    <svg width="28" height="20" viewBox="0 0 28 20"><path d="M2 7 A17 17 0 0 1 26 7" fill="none" stroke="#aaaaaa" stroke-width="3"/><path d="M7 12 A10 10 0 0 1 21 12" fill="none" stroke="#aaaaaa" stroke-width="3"/><circle cx="14" cy="17" r="2.5" fill="#aaaaaa"/></svg>
    <svg width="38" height="16" viewBox="0 0 38 16"><rect x="1" y="1" width="32" height="14" rx="3" fill="none" stroke="#aaaaaa" stroke-width="1.5"/><rect x="4" y="4" width="26" height="8" rx="1.5" fill="#aaaaaa"/><rect x="34.5" y="5" width="2.5" height="6" fill="#aaaaaa"/></svg>
  </div>

  <svg class="menu-button" viewBox="0 0 34 24" role="img" aria-label="Settings menu">
    <line x1="0" y1="2" x2="34" y2="2" stroke="#1b1b1b" stroke-width="2"/>
    <line x1="0" y1="12" x2="34" y2="12" stroke="#1b1b1b" stroke-width="2"/>
    <line x1="0" y1="22" x2="34" y2="22" stroke="#1b1b1b" stroke-width="2"/>
  </svg>
  <svg class="contact-button" viewBox="0 0 36 28" role="img" aria-label="Contact">
    <rect x="1" y="1" width="34" height="26" fill="none" stroke="#2f6fc0" stroke-width="2"/>
    <polyline points="1,1 18,16 35,1" fill="none" stroke="#2f6fc0" stroke-width="2"/>
    <line x1="1" y1="27" x2="14" y2="13" stroke="#2f6fc0" stroke-width="2"/>
    <line x1="35" y1="27" x2="22" y2="13" stroke="#2f6fc0" stroke-width="2"/>
  </svg>

  <header class="brand">
    <div class="brand-circle" aria-hidden="true"></div>
    <h1 class="brand-name">SkyVelour</h1>
  </header>

  <section class="route">
    <div class="route-rule top-left"></div>
    <div class="route-rule top-right"></div>
    <div class="route-rule bottom-left"></div>
    <div class="route-rule bottom-right"></div>

    <div class="airport departure">
      <div class="airport-label">Departure</div>
      <div class="airport-code">JFK</div>
    </div>
    <svg class="go-button" viewBox="0 0 78 78" role="img" aria-label="Calculate flight">
      <circle cx="39" cy="39" r="37" fill="#e4e4e2" stroke="#8a8a8a" stroke-width="2"/>
      <circle cx="39" cy="39" r="32" fill="none" stroke="#c4c4c4" stroke-width="1"/>
      <polygon points="29,25 55,39 29,53 34,39" fill="none" stroke="#5c5c5c" stroke-width="2" stroke-linejoin="round"/>
    </svg>
    <div class="airport destination">
      <div class="airport-label">Destination</div>
      <div class="airport-code">LAX</div>
    </div>
    <div class="aircraft-code">AL757</div>
  </section>

  <section class="details">
    <div class="detail-row"><span class="detail-label">Distance:</span><span class="detail-value">2,826 mi</span></div>
    <div class="detail-row"><span class="detail-label">Flight time:</span><span class="detail-value">6h 30m</span></div>
    <div class="detail-row aircraft"><span class="detail-label">Aircraft:</span><span class="detail-value">Altair 757</span></div>
    <div class="gallery">
      <div class="gallery-photo exterior" role="img" aria-label="Aircraft exterior, front view"></div>
      <div class="gallery-photo runway" role="img" aria-label="Aircraft on the runway"></div>
      <div class="gallery-photo exterior" role="img" aria-label="Aircraft fuselage side view"></div>
      <div class="gallery-photo stairs" role="img" aria-label="Aircraft boarding stairs"></div>
      <div class="gallery-photo cabin" role="img" aria-label="Cabin aisle interior"></div>
      <div class="gallery-photo cabin" role="img" aria-label="Cabin seating interior"></div>
    </div>
  </section>

  <div class="home-indicator" aria-hidden="true"></div>
</main>
</body>
</html>
```